Soccer Club Site Redesign

We are a suburban youth soccer club in need of a web site redesign. Our current site’s look/feel is outdated and is in need of a more modern look. What we are looking for is a design layout that will accommodate the current functionality we have for the site and give us an updated modern look. The deliverable for this project will be .psd file that can be converted to an html theme file for Wordpress. We will take care of the conversion and handle the html coding/javascript functionality.
Take a look at our current site to get an idea of what we offer and the current layout we have.
http://www.fernwickfootball.org
Our club hosts youth recreational soccer, traveling soccer and two large soccer tournaments during the year. We also sponsor a number of training clinics. Our site serves a couple primary purposes:
1. Parents learn how/where/when to sign up their child for the leagues we offer.
2. Parents learn dates/times of various events the club offers.
3. Other soccer clubs get information on the tournaments we offer, sign up for the tournaments etc.
We do a pretty good job of presenting information about the various events/leagues available and how to sign up for them, but we want to do a better job of presenting a calendar where parents can quickly find dates/times of various events. Ideally, we would like to incorporate a news section (like we currently have), with a calendar and the use of more images on the home page. We understand screen space is limited but would incorporate jquery/javascript widgets to hide/show info and maybe an ‘imagebox’ for the additional images.
Here are a few sites with ideas that we liked:
http://sports.dorrington.edu/ (Look at the Upcoming Events calendar on the page)
http://www.ashvalekickers.com/ (look at the Upcoming Events calendar in the right column and the image box in the main content area)
http://www.plumetfutbol.com/index.php (Like the look and use of images)
http://www.rqkickersclub.com/ (imagebox use)
http://www.lorvanpuckclub.org/ ( hockey website but like the use of crisp header graphics)
http://www.ellisfordpuck.com/ (another hockey site, like the calendar used)
That should give you a pretty good idea of what we are looking for. The new design will need to accommodate the existing functionality of the site. Our logo (which is attached) should be incorporated into the site….otherwise we are open to your design ideas.

```html
<!DOCTYPE html>
<html lang="en">
<head>
<meta charset="utf-8">
<title>Fernwick Football Club</title>
<link href="https://fonts.googleapis.com/css2?family=Roboto:wght@300;400;500&family=Arimo:wght@400;700&display=swap" rel="stylesheet">
<style>
:root{
  --grass-dark:#0b1508;
  --grass:#2c4a1c;
  --page:#000;
  --nav:#111;
  --panel:#333;
  --rule:#4a4a4a;
  --white:#fff;
  --muted:#d8d8d8;
  --orange:#f5a300;
  --btn-top:#ffb41a;
  --btn-bottom:#f07a00;
  --club-blue:#1f63b0;
}
*{margin:0;padding:0;box-sizing:border-box}
html,body{width:854px;height:1200px;overflow:hidden}
body{
  position:relative;
  background:radial-gradient(ellipse at 50% 0%,var(--grass) 0%,#1a2d10 45%,var(--grass-dark) 100%);
  font-family:"Arimo",Arial,sans-serif;color:var(--white);
}
.abs{position:absolute}
.social{left:642px;top:69px;display:flex;align-items:center;gap:8px;font-size:10px}
.social .square{width:21px;height:21px;background:var(--club-blue);border-radius:3px}
.site{left:91px;top:98px;width:671px;height:1055px;background:var(--page)}
.nav{left:0;top:0;width:671px;height:42px;background:var(--nav);border-radius:6px 6px 0 0;border-bottom:2px solid var(--white)}
.nav a{position:absolute;top:13px;color:var(--white);text-decoration:none;font-size:14px;white-space:nowrap}
.nav .current::after{content:"";position:absolute;left:50%;bottom:-15px;margin-left:-6px;border:6px solid transparent;border-bottom-color:var(--white)}
.club-name{left:274px;top:-38px;width:121px;display:flex;flex-direction:column;align-items:center;gap:8px;z-index:3;text-align:center;font-family:"Roboto",sans-serif;font-weight:500;font-size:15px;line-height:17px;color:var(--white)}
.club-name .dot{width:30px;height:30px;border-radius:50%;background:var(--club-blue)}
.hero{left:0;top:42px;width:671px;height:333px;background:
  radial-gradient(ellipse at 70% 40%,rgba(60,140,210,.55),transparent 45%),
  linear-gradient(180deg,#2a2420 0%,#5a4a38 30%,#1c1e22 60%,#0c0e10 100%)}
.hero h1{left:20px;top:190px;font-family:"Arimo",sans-serif;font-weight:400;font-size:43px;line-height:42px;color:var(--white)}
.dots{left:22px;top:312px;display:flex;gap:4px}
.dots span{width:11px;height:11px;border-radius:50%;background:#555}
.dots span.on{background:#aaa}
h2{font-family:"Roboto",sans-serif;font-weight:300;font-size:28px;line-height:32px;color:var(--white);letter-spacing:.3px;white-space:nowrap}
p{font-size:12px;line-height:15px}
.lead{color:var(--orange);text-transform:uppercase;font-size:11.5px;line-height:15px}
.btn{display:block;width:119px;height:30px;border-radius:5px;background:linear-gradient(var(--btn-top),var(--btn-bottom));color:var(--white);font-size:15px;line-height:30px;text-align:center;text-decoration:none}
.photo{background:linear-gradient(135deg,#9a8a60,#c8b890 45%,#6e7a48);border:2px solid #ddd}
.divider{left:21px;top:683px;width:405px;border-top:1px dotted #888}
.team-photo{left:21px;top:782px;width:410px;height:176px;border:2px solid var(--white);border-radius:8px;background:linear-gradient(180deg,#4d7a3a 0%,#1f4a2c 40%,#174028 80%,#3c7a34 100%)}
.sidebar{left:450px;top:407px;width:194px;height:625px;background:var(--panel);border-radius:6px}
.sidebar h3{font-family:"Roboto",sans-serif;font-weight:400;font-size:18px;line-height:22px;position:absolute;left:8px;white-space:nowrap}
.event{position:absolute;left:8px;width:178px;height:46px;border-top:1px solid var(--rule)}
.event svg{position:absolute;left:0;top:10px}
.event .match{position:absolute;left:33px;top:15px;font-size:10px;line-height:12px;text-transform:uppercase;white-space:nowrap}
.event .when{position:absolute;left:33px;top:29px;font-size:7px;line-height:9px;text-transform:uppercase;white-space:nowrap}
.coach-photo{position:absolute;left:9px;width:92px;height:80px;border:2px solid var(--white);border-radius:4px;background:linear-gradient(160deg,#6f7a6a,#3b3f3a 60%,#2c2e30)}
.coach-name{position:absolute;left:108px;font-size:14px;line-height:16px;white-space:nowrap}
.coach-role{position:absolute;left:108px;font-size:7px;line-height:9px;white-space:nowrap}
.coach-bio{position:absolute;left:11px;width:178px;font-size:8px;line-height:11.5px;color:var(--muted)}
.footer{left:0;top:1153px;width:854px;height:47px;background:var(--page);text-align:center;font-size:11px;line-height:47px;text-transform:uppercase}
</style>
</head>
<body>
<div class="abs social"><span class="square"></span><span>Join Us on Friendspace</span></div>

<div class="abs site">
  <nav class="abs nav">
    <a class="current" style="left:18px" href="#">Home</a>
    <a style="left:83px" href="#">About us</a>
    <a style="left:168px" href="#">Recreational</a>
    <a style="left:421px" href="#">Tournaments</a>
    <a style="left:525px" href="#">Referees</a>
    <a style="left:603px" href="#">Contact</a>
  </nav>
  <div class="abs club-name"><span>Fernwick<br>Football Club</span><span class="dot"></span></div>

  <section class="abs hero" role="img" aria-label="Player in a blue kit striking a ball in a floodlit stadium">
    <h1 class="abs">Play Like a<br>Champion Today</h1>
    <div class="abs dots"><span></span><span class="on"></span><span></span></div>
  </section>

  <section class="abs welcome" style="left:21px;top:407px;width:200px">
    <h2>WELCOME</h2>
    <p class="lead" style="margin-top:4px">Tempor incididunt ut labore et dolore magna aliqua. Ut enim ad minim veniam</p>
    <p style="margin-top:14px">Incididunt ut labore et dolore magna aliqua. Ut enim ad minim veniam, quis nostrud exercitation ullamco laboris nisi ut aliquip ex ea commodo consequat.</p>
    <p style="margin-top:14px">Duis aute irure dolor in reprehenderit in voluptate velit esse cillum.</p>
  </section>
  <a class="abs btn" style="left:22px;top:635px" href="#">Read More</a>

  <section class="abs about" style="left:247px;top:407px;width:194px">
    <h2>ABOUT</h2>
    <div class="photo" style="width:182px;height:100px;margin-top:0" role="img" aria-label="Youth player in orange kicking the ball past a goalkeeper"></div>
    <p style="margin-top:14px;width:192px">Incididunt ut labore et dolore magna aliqua. Ut enim ad minim veniam, quis nostrud exercitation ullamco laboris</p>
  </section>
  <a class="abs btn" style="left:250px;top:635px" href="#">Read More</a>

  <div class="abs divider"></div>
  <h2 class="abs" style="left:21px;top:694px">OUR NEW SOCCER TEAMS</h2>
  <p class="abs" style="left:21px;top:749px;width:415px">Incididunt ut labore et dolore magna aliqua. Ut enim ad minim veniam, quis nostrud exercitation ullamco laboris nisi ut aliquip ex ea commodo consequat.</p>
  <div class="abs team-photo" role="img" aria-label="Group photo of a girls team in green kits with their coaches"></div>
  <p class="abs" style="left:21px;top:977px;width:415px">Incididunt ut labore et dolore magna aliqua. Ut enim ad minim veniam, quis nostrud exercitation ullamco laboris nisi ut aliquip ex ea commodo consequat.</p>
  <p class="abs" style="left:21px;top:1020px;width:415px">Duis aute irure dolor in reprehenderit in voluptate velit esse cillum.</p>

  <aside class="abs sidebar">
    <h3 style="top:18px">UPCOMING EVENTS</h3>
    <div class="event" style="top:50px">
      <svg width="23" height="27" viewBox="0 0 23 27"><rect x="1" y="3" width="21" height="23" rx="2" fill="#fff"/><rect x="1" y="3" width="21" height="6" rx="2" fill="#3a8ad6"/><rect x="5" y="0" width="2" height="6" fill="#999"/><rect x="16" y="0" width="2" height="6" fill="#999"/><text x="11.5" y="23" font-family="Arimo,sans-serif" font-size="12" font-weight="700" text-anchor="middle" fill="#222">12</text></svg>
      <span class="match">FC Ipsum - ACS Moldren</span><span class="when">20:00, October 29</span>
    </div>
    <div class="event" style="top:96px">
      <svg width="23" height="27" viewBox="0 0 23 27"><rect x="1" y="3" width="21" height="23" rx="2" fill="#fff"/><rect x="1" y="3" width="21" height="6" rx="2" fill="#3a8ad6"/><rect x="5" y="0" width="2" height="6" fill="#999"/><rect x="16" y="0" width="2" height="6" fill="#999"/><text x="11.5" y="23" font-family="Arimo,sans-serif" font-size="12" font-weight="700" text-anchor="middle" fill="#222">12</text></svg>
      <span class="match">ACS Stelara - AC Crew</span><span class="when">17:00, November 1</span>
    </div>
    <div class="event" style="top:142px">
      <svg width="23" height="27" viewBox="0 0 23 27"><rect x="1" y="3" width="21" height="23" rx="2" fill="#fff"/><rect x="1" y="3" width="21" height="6" rx="2" fill="#3a8ad6"/><rect x="5" y="0" width="2" height="6" fill="#999"/><rect x="16" y="0" width="2" height="6" fill="#999"/><text x="11.5" y="23" font-family="Arimo,sans-serif" font-size="12" font-weight="700" text-anchor="middle" fill="#222">12</text></svg>
      <span class="match">Dynamo Z - Young Foxes</span><span class="when">14:00, November 2</span>
    </div>
    <div class="event" style="top:190px;border-bottom:1px solid var(--rule)">
      <svg width="23" height="27" viewBox="0 0 23 27"><rect x="1" y="3" width="21" height="23" rx="2" fill="#fff"/><rect x="1" y="3" width="21" height="6" rx="2" fill="#3a8ad6"/><rect x="5" y="0" width="2" height="6" fill="#999"/><rect x="16" y="0" width="2" height="6" fill="#999"/><text x="11.5" y="23" font-family="Arimo,sans-serif" font-size="12" font-weight="700" text-anchor="middle" fill="#222">12</text></svg>
      <span class="match">Nayan - Zarvec</span><span class="when">20:00, October 29</span>
    </div>

    <h3 style="top:252px">OUR COACHES</h3>
    <div class="coach-photo" style="top:289px" role="img" aria-label="Portrait of the goalkeeper coach"></div>
    <span class="coach-name" style="top:323px">Mark DUNN</span>
    <span class="coach-role" style="top:341px">Goalkeeper Coach</span>
    <p class="coach-bio" style="top:384px">Lorem ipsum dolor sit amet, consectetur adipiscing elit. Cras auctor urna et diam rutrum bibendum. In auctor, sem eget commodo pharetra, diam odio adipiscing enim,</p>
    <div class="abs" style="left:8px;top:440px;width:178px;border-top:1px solid var(--rule)"></div>
    <div class="coach-photo" style="top:454px" role="img" aria-label="Portrait of the midfielders coach"></div>
    <span class="coach-name" style="top:488px">Harris COLT</span>
    <span class="coach-role" style="top:506px">Midfielders Coach</span>
    <p class="coach-bio" style="top:551px">Lorem ipsum dolor sit amet, consectetur adipiscing elit. Cras auctor urna et diam rutrum bibendum. In auctor, sem eget commodo pharetra, diam odio adipiscing enim,</p>
  </aside>
</div>

<footer class="abs footer">2012 Fernwick Football Club Copyright. All Rights Reserved</footer>
</body>
</html>
```